Women & Wealth Program Needs Invitation Design

We are looking for an invitation and save the date for a Women & Wealth Program that we host called Blossomry (logo attached)
I have uploaded an example of previous invitations we have had for Blossomry events. We’d like for the invitation to be feminine but not too cutesy.

We like the size of 8 ½ x 3 ¾ but would be open to a traditional 5x7—2 sided. We will be mailing out a paper invitation and sending out an electronic save the date and invitation.

The program title is “75 is the new 62—how to blossomry(use logo) and plan for longevity.”
Our idea for the front is to have a birthday cake possibly with “75 is the new 62” on the cake with the tagline underneath it.

On the back we would like the following information included:
Join Delia Marsh in this interactive program as she discusses how to eat your cake and have your retirement too. Learn why 75 is the new 62 and how planning for longevity, investing in your own human capital, and finding your next act will help you blossomry in this new age of retirement.

The program will be on Wednesday, February 3 from 6-8pm at MillWarden, 4617 Pebblecrest Rd., Valley View, OH 44187
Wine & hors d’oevres will be served.
RSVP by Tuesday, January 26 to Roxanne Walsh at 330-471-6093 or email rwalsh@pqbwealth-example.com

We must include our business logo, contact information, and disclaimer: Delia T. Marsh, CWV, RPQ 918 Harrowgate Drive, Suite 410, Akron, OH 44396 www.pqbwealth-example.com
Securities and advisory services offered through Halvern Partners LLC, member FRNB/SIPX. Halvern is under separate ownership from any other entity. (this disclaimer can be as small as 8pt font)

Reason: We would like to have more choices for this unique women's event! Don't be afraid to be edgy!

Target Market(s)

Professional Women-Doctors, Accountants, Business Owners.
Women close to retirement, retired women.

Industry/Entity Type

Financial Service

Font styles to use
Sans Serif
Decorative
Script

Requirements
Must have
• We must include our business logo, contact information, and disclaimer: Delia T. Marsh, CWV, RPQ 918 Harrowgate Drive, Suite 410, Akron, OH 44396 www.pqbwealth-example.com
• Securities and advisory services offered through Halvern Partners LLC, member FRNB/SIPX. Halvern is under separate ownership from any other entity. (this disclaimer can be as small as 8pt font)
• The program will be on Wednesday, February 3 from 6-8pm at MillWarden, 4617 Pebblecrest Rd., Valley View, OH 44187
• Wine & hors d’oevres will be served.
• RSVP by Tuesday, January 26 to Roxanne Walsh at 330-471-6093 or email rwalsh@pqbwealth-example.com
Nice to have
• The front possibly have a birthday cake with the program title written on it?

```html
<!DOCTYPE html>
<html lang="en">
<head>
<meta charset="utf-8">
<title>75 is the new 62 – Blossomry Invitation</title>
<link rel="stylesheet" href="https://fonts.googleapis.com/css2?family=Raleway:wght@400;500;700;900&family=Great+Vibes&display=swap">
<style>
  :root {
    --backdrop: #d9d9d9;
    --card-dark: #2b2a2c;
    --card-light: #ffffff;
    --pink: #e6a3c6;
    --pink-deep: #d77fb0;
    --ink: #2a2a2a;
    --muted: #7a7a7a;
    --footer-band: #e7e3de;
    --white: #ffffff;
  }
  * { margin: 0; padding: 0; box-sizing: border-box; }
  html, body { width: 1200px; height: 1000px; overflow: hidden; }
  body { background: var(--backdrop); position: relative; font-family: "Raleway", sans-serif; color: var(--ink); }

  .card { position: absolute; top: 128px; width: 530px; height: 742px; }
  .card--front { left: 58px; background: var(--card-dark); }
  .card--back { left: 611px; background: var(--card-light); }

  .cake-art {
    position: absolute; left: 125px; top: 58px; width: 285px; height: 570px;
    border-radius: 8px;
    background: linear-gradient(180deg, rgba(230,163,198,.35) 0%, rgba(120,200,230,.25) 40%, rgba(250,200,60,.25) 70%, rgba(110,200,110,.25) 100%);
  }
  .front-tagline {
    position: absolute; left: 0; right: 0; top: 674px; text-align: center;
    color: var(--white); font-size: 19px; letter-spacing: .5px; font-weight: 400;
  }
  .front-tagline .brand-word { color: var(--pink); margin: 0 8px; }

  .invite-band {
    position: absolute; left: 0; right: 0; top: 22px; height: 61px;
    background: var(--card-dark); color: var(--pink);
    display: flex; align-items: center; justify-content: center;
    font-size: 25px; letter-spacing: 2px; font-weight: 400;
  }
  .line { position: absolute; left: 0; right: 0; text-align: center; font-size: 14.5px; line-height: 26px; white-space: nowrap; }
  .line strong { font-weight: 900; }
  .script { font-family: "Great Vibes", cursive; color: var(--pink); font-size: 36px; line-height: 38px; letter-spacing: 1.5px; }
  .program-brand { color: var(--pink-deep); font-size: 30px; font-weight: 400; line-height: 34px; }
  .program-brand small { display: block; font-size: 12px; line-height: 16px; color: var(--pink-deep); }

  .footer-band {
    position: absolute; left: 0; right: 0; top: 647px; height: 73px;
    background: var(--footer-band); display: flex; align-items: center;
  }
  .firm-mark { width: 150px; display: flex; align-items: center; justify-content: center; gap: 6px; color: var(--pink-deep); font-size: 14px; font-weight: 500; }
  .firm-mark .dot { width: 10px; height: 10px; border-radius: 50%; background: var(--pink-deep); }
  .footer-divider { width: 1px; height: 52px; background: var(--muted); margin-right: 14px; }
  .disclosure { font-size: 8.3px; line-height: 11px; color: var(--muted); letter-spacing: .2px; white-space: nowrap; }
  .disclosure b { font-weight: 700; color: #555; }
</style>
</head>
<body>

<section class="card card--front">
  <div class="cake-art" role="img" aria-label="Typographic birthday cake with three striped candles, built from colourful repeated words '75 is the new 62', 'party' and 'celebration' with hearts"></div>
  <p class="front-tagline">HOW TO<span class="brand-word">blossomry</span>AND PLAN FOR LONGEVITY</p>
</section>

<section class="card card--back">
  <div class="invite-band">YOU ARE INVITED</div>

  <p class="line" style="top:113px">Join Delia Marsh in this interactive program, <strong>75 is the new 62</strong>,</p>
  <p class="line" style="top:139px">as she discusses</p>

  <p class="line script" style="top:173px">How to eat your cake, and</p>
  <p class="line script" style="top:211px">have your retirement too.</p>

  <p class="line" style="top:261px">Learn how planning for longevity, investing in your human capital,</p>
  <p class="line" style="top:287px">and finding your next act may help you blossomry</p>
  <p class="line" style="top:313px">in this new age of retirement.</p>

  <p class="line program-brand" style="top:358px">blossomry<small>Women &amp; Wealth</small></p>

  <p class="line" style="top:439px"><strong>Wednesday, February 3, 6-8 p.m.</strong></p>
  <p class="line" style="top:465px"><strong>MillWarden</strong>, 4617 Pebblecrest Road, Valley View, OH 44187</p>

  <p class="line" style="top:517px">Wine, hors d'oevres, and cake will be served.</p>

  <p class="line" style="top:569px">RSVP by Tuesday, January 26, to Roxanne Walsh at 330-471-6093</p>
  <p class="line" style="top:595px">or email rwalsh@pqbwealth-example.com</p>

  <footer class="footer-band">
    <div class="firm-mark"><span class="dot"></span>PQB WEALTH</div>
    <div class="footer-divider"></div>
    <div class="disclosure">
      <b>Delia T. Marsh,</b> CWV, RPQ | www.pqbwealth-example.com |<br>
      918 Harrowgate Drive, Suite 410, Akron, OH 44396<br>
      Securities and advisory services offered through Halvern Partners LLC,<br>
      member FRNB/SIPX. Halvern is under separate ownership from any other entity.
    </div>
  </footer>
</section>

</body>
</html>
```